Stationery & Business Card Design Project

We require our stationary to be professional, which will stand out but also be sophisticated and reputable.

We also require the following:

* Business card must be double sided
* Logo must stand out with brightnest colours used. Other colours may be added but only in small doses as not to overtake the main colours.
* For business card brightnest pty ltd smsf specialists with administrators at bottom left on the front of the card and details on the back

Industry/Entity Type

Business

Requirements
Must have
• * Business Cards
* With compliments slips –2 different ones
* Forwarding mail slip (smaller version of a with compliments slip)

```html
<!DOCTYPE html>
<html lang="en">
<head>
<meta charset="utf-8">
<title>brightnest stationery</title>
<link href="https://fonts.googleapis.com/css2?family=Source+Sans+3:wght@400;600;700&display=swap" rel="stylesheet">
<style>
  :root {
    --navy: #2b3580;
    --grey: #6d6e70;
    --grey-light: #a7a9ac;
    --paper: #ffffff;
    --stage: #000000;
    --text: #58595b;
  }
  * { margin: 0; padding: 0; box-sizing: border-box; }
  html, body { width: 900px; height: 1200px; overflow: hidden; background: var(--stage); }
  body { position: relative; font-family: "Source Sans 3", Arial, sans-serif; color: var(--text); }

  .piece { position: absolute; overflow: hidden; background: var(--paper); }

  .brand { position: absolute; display: flex; align-items: center; }
  .brand__square { background: var(--grey); flex: none; border-radius: 3px; }
  .brand__name { font-weight: 600; color: var(--navy); letter-spacing: -0.02em; line-height: 1; }

  .edge-bar { position: absolute; left: 0; bottom: 0; width: 100%; display: block; }

  /* business card front */
  .card-front { left: 35px; top: 79px; width: 354px; height: 214px; }
  .card-front .holder { position: absolute; left: 18px; top: 46px; }
  .holder__name { font-size: 13px; font-weight: 700; color: var(--navy); }
  .holder__role { font-size: 11px; color: var(--grey); margin-top: 1px; }
  .contact-list { position: absolute; left: 16px; top: 103px; list-style: none; font-size: 8.5px; line-height: 11.2px; color: var(--text); }
  .contact-list li { display: flex; align-items: center; gap: 5px; }
  .contact-list svg { width: 7px; height: 7px; fill: var(--navy); flex: none; }
  .card-front .brand { left: 174px; top: 80px; gap: 7px; }
  .card-front .brand__square { width: 40px; height: 40px; }
  .card-front .brand__name { font-size: 22px; }

  /* business card back */
  .card-back { left: 408px; top: 79px; width: 355px; height: 214px; background: var(--navy); }
  .card-back .split { position: absolute; inset: 0; width: 100%; height: 100%; }
  .card-back .brand { left: 28px; top: 86px; gap: 8px; }
  .card-back .brand__square { width: 40px; height: 40px; background: var(--paper); }
  .card-back .brand__name { font-size: 30px; color: var(--paper); }

  /* compliments slip */
  .slip { left: 35px; top: 322px; width: 827px; height: 389px; }
  .slip .brand { left: 32px; top: 30px; gap: 10px; }
  .slip .brand__square { width: 66px; height: 66px; }
  .slip .brand__name { font-size: 38px; }
  .slip__divider { position: absolute; left: 312px; top: 31px; width: 1px; height: 68px; background: var(--grey-light); }
  .slip__address { position: absolute; left: 329px; top: 55px; font-size: 14px; color: var(--grey); }
  .slip__title { position: absolute; left: 39px; top: 118px; font-size: 27px; font-weight: 600; color: var(--navy); }
  .slip__title span { color: var(--grey); }
  .slip__web { position: absolute; right: 10px; top: 346px; font-size: 14px; letter-spacing: 0.06em; color: #231f20; }

  /* cover */
  .cover { left: 35px; top: 728px; width: 827px; height: 390px; background: var(--navy); }
  .cover .split { position: absolute; inset: 0; width: 100%; height: 100%; }
  .cover .brand { left: 130px; top: 188px; gap: 14px; }
  .cover .brand__square { width: 104px; height: 104px; background: var(--paper); border-radius: 6px; }
  .cover .brand__name { font-size: 62px; color: var(--paper); }
</style>
</head>
<body>

  <section class="piece card-front">
    <div class="holder">
      <p class="holder__name">Claire Hollings</p>
      <p class="holder__role">Independent Distributor</p>
    </div>
    <ul class="contact-list">
      <li><svg viewBox="0 0 10 10"><rect x="1" y="1" width="8" height="8" rx="1"/></svg>PO Box 318, Karama, NT 0812</li>
      <li><svg viewBox="0 0 10 10"><path d="M0 2h10v6H0z"/></svg>claire@brightnest.com.au</li>
      <li><svg viewBox="0 0 10 10"><path d="M3 0h4v10H3z"/></svg>0491 570 156</li>
      <li><svg viewBox="0 0 10 10"><path d="M1 3h8v5H1zM3 1h4v2H3z"/></svg>1300 555 014</li>
      <li><svg viewBox="0 0 10 10"><circle cx="5" cy="5" r="4.5"/></svg>www.brightnest.com.au</li>
    </ul>
    <div class="brand">
      <span class="brand__square"></span>
      <span class="brand__name">brightnest</span>
    </div>
    <svg class="edge-bar" viewBox="0 0 354 7" height="7" preserveAspectRatio="none">
      <polygon points="0,0 274,0 268,7 0,7" fill="var(--navy)"/>
      <polygon points="276,0 354,0 354,7 270,7" fill="var(--grey)"/>
    </svg>
  </section>

  <section class="piece card-back">
    <svg class="split" viewBox="0 0 355 214" preserveAspectRatio="none">
      <polygon points="250,0 355,0 355,214 200,214" fill="var(--grey)"/>
    </svg>
    <div class="brand">
      <span class="brand__square"></span>
      <span class="brand__name">brightnest</span>
    </div>
  </section>

  <section class="piece slip">
    <div class="brand">
      <span class="brand__square"></span>
      <span class="brand__name">brightnest</span>
    </div>
    <span class="slip__divider"></span>
    <p class="slip__address">PO Box 318, Karama, NT 0812</p>
    <h1 class="slip__title">With <span>Compliments</span></h1>
    <p class="slip__web">www.brightnest.com.au</p>
    <svg class="edge-bar" viewBox="0 0 827 16" height="16" preserveAspectRatio="none">
      <polygon points="0,0 556,0 542,16 0,16" fill="var(--navy)"/>
      <polygon points="560,0 827,0 827,16 546,16" fill="var(--grey)"/>
    </svg>
  </section>

  <section class="piece cover">
    <svg class="split" viewBox="0 0 827 390" preserveAspectRatio="none">
      <polygon points="600,0 827,0 827,390 470,390" fill="var(--grey)"/>
    </svg>
    <div class="brand">
      <span class="brand__square"></span>
      <span class="brand__name">brightnest</span>
    </div>
  </section>

</body>
</html>
```